Naturopath Practitioner Card Design

I am a naturopath needing a design for a business card mainly to show that I am a naturopath and have some contact details to give to prospective clients. I am open minded about the design and what is on the second side of the card whether it just be some artwork or space for details, appointment times etc. Naturopathy is the practice of natural medicine that uses a holistic approach and incorporates herbal and nutritional medicine.

Contact Information for Business Card

Tom Waverly NaturopathBHSc (Naturopathy) Member NHPG 0491 582 736 tom.waverly@mailbox-example.net www.tomwaverlynaturopathy.example.au

Requirements
Nice to have
• Would prefer some kind of original pattern/art work/logo rather than an image, not fussed if its very simple/basic
• I am open to any colour but think I would prefer a more earthy sandy clay etc type style than the greens that are commonly associated with naturopathy.
Should not have
• Don't really want to have generic stock images on it

```html
<!DOCTYPE html>
<html lang="en">
<head>
<meta charset="utf-8">
<title>Tom Waverly – Naturopath Cards</title>
<link rel="stylesheet" href="https://fonts.googleapis.com/css2?family=Arimo:wght@400;700&family=Tinos:wght@700&display=swap">
<style>
  :root {
    --page: #ece8e1;
    --card: #fbfbfa;
    --card-edge: #dcdad5;
    --ink: #111111;
    --dots: #444444;
    --stone-tone: rgba(214, 210, 196, 0.75);
    --water-tone: rgba(226, 225, 220, 0.6);
  }
  * { box-sizing: border-box; margin: 0; padding: 0; }
  html, body {
    width: 1200px; height: 864px; overflow: hidden;
    background: var(--page);
    font-family: "Arimo", Arial, sans-serif;
    color: var(--ink);
  }
  .sheet {
    width: 1200px; height: 864px;
    display: flex; flex-direction: column; align-items: center; justify-content: center;
    gap: 34px;
  }
  .card {
    position: relative;
    width: 665px; height: 380px;
    background: var(--card);
    border: 1px solid var(--card-edge);
    box-shadow: 0 6px 18px rgba(0,0,0,0.12);
    overflow: hidden;
  }

  /* Front */
  .front-art {
    position: absolute; inset: 0;
    background: radial-gradient(ellipse 260px 220px at 150px 190px, var(--stone-tone) 0%, rgba(214,210,196,0.35) 45%, rgba(251,251,250,0) 100%);
  }
  .front-details {
    position: absolute; right: 40px; top: 112px;
    text-align: right;
  }
  .front-details .name { font-size: 44px; font-weight: 700; line-height: 1.05; }
  .front-details .role { font-size: 24px; line-height: 1.2; margin-top: 4px; }
  .front-details .credentials { font-size: 20px; line-height: 1.3; }
  .contact {
    position: absolute; right: 40px; bottom: 28px;
    display: flex; flex-direction: column; align-items: flex-end; gap: 5px;
    font-size: 20px;
  }
  .contact-line { display: flex; align-items: center; gap: 10px; line-height: 1.2; }
  .contact-line svg { width: 18px; height: 18px; flex: none; }

  /* Back */
  .back-art {
    position: absolute; inset: 0;
    background: radial-gradient(ellipse 300px 190px at 90px 360px, var(--water-tone) 0%, rgba(226,225,220,0.25) 50%, rgba(251,251,250,0) 100%);
  }
  .appointment { position: absolute; inset: 0; padding: 36px 40px 0 40px; }
  .appointment h2 {
    font-family: "Tinos", "Times New Roman", serif;
    font-size: 46px; font-weight: 700;
    text-align: right; padding-right: 40px;
    line-height: 1;
  }
  .field-row { display: flex; align-items: flex-end; font-size: 19px; font-weight: 700; margin-top: 14px; }
  .field-row .label { white-space: nowrap; }
  .dotted { flex: 1; border-bottom: 2px dotted var(--dots); margin: 0 6px 4px 4px; }
  .days { display: flex; justify-content: space-between; margin-top: 22px; font-size: 19px; }
  .day { display: flex; align-items: center; gap: 4px; }
  .box { width: 16px; height: 16px; border: 1.5px solid var(--ink); }
  .blank-line { border-bottom: 2px dotted var(--dots); margin-top: 30px; }
</style>
</head>
<body>
<main class="sheet">

  <section class="card card-front">
    <div class="front-art" role="img" aria-label="Stacked pale pebbles and wild grass stems reflected in still water"></div>
    <div class="front-details">
      <p class="name">Tom Waverly</p>
      <p class="role">Naturopath</p>
      <p class="credentials">BHSc (Naturopathy) Member NHPG</p>
    </div>
    <div class="contact">
      <p class="contact-line">0491 582 736
        <svg viewBox="0 0 18 18" aria-hidden="true"><rect x="1" y="1" width="16" height="16" rx="2" fill="#111"/><path d="M5 5c0 5 3 8 8 8l1-2-2-1-1 1c-2-1-3-2-4-4l1-1-1-2z" fill="#fff"/></svg>
      </p>
      <p class="contact-line">tom.waverly@mailbox-example.net
        <svg viewBox="0 0 18 18" aria-hidden="true"><rect x="1" y="1" width="16" height="16" rx="2" fill="#111"/><rect x="4" y="5.5" width="10" height="7" fill="#fff"/><path d="M4 5.5l5 4 5-4" stroke="#111" fill="none"/></svg>
      </p>
      <p class="contact-line">www.tomwaverlynaturopathy.example.au
        <svg viewBox="0 0 18 18" aria-hidden="true"><rect x="1" y="1" width="16" height="16" rx="2" fill="#111"/><circle cx="9" cy="9" r="5" stroke="#fff" stroke-width="1.2" fill="none"/><path d="M4 9h10M9 4c-2.5 3-2.5 7 0 10M9 4c2.5 3 2.5 7 0 10" stroke="#fff" stroke-width="1" fill="none"/></svg>
      </p>
    </div>
  </section>

  <section class="card card-back">
    <div class="back-art" role="img" aria-label="Faint rippling water reflection of grass stems"></div>
    <div class="appointment">
      <h2>Appointment</h2>
      <div class="field-row"><span class="label">For:</span><span class="dotted"></span></div>
      <div class="field-row"><span class="label">Date:</span><span class="dotted"></span><span class="label">Time:</span><span class="dotted"></span></div>
      <div class="days">
        <span class="day"><span class="box"></span>MON.</span>
        <span class="day"><span class="box"></span>TUE.</span>
        <span class="day"><span class="box"></span>WED.</span>
        <span class="day"><span class="box"></span>THUR.</span>
        <span class="day"><span class="box"></span>FRI.</span>
        <span class="day"><span class="box"></span>SAT.</span>
      </div>
      <div class="blank-line"></div>
      <div class="blank-line"></div>
      <div class="blank-line"></div>
    </div>
  </section>

</main>
</body>
</html>
```